Graphic Design Set for Banner Ads - Sizes and Specs for Bidlane

We need a set of 6 ads of the following sizes created for Bidlane:

Medium rectangle: 300×250
Leaderboard: 728×90
Wide skyscraper: 160×600
Large rectangle: 300x600
Mobile leaderboard: 320×50

Here are the Formatting Guidelines (WEB ADS): https://help.bidlane.com/hc/en-us/articles/583920147-Ad-Content-and-Format-Guidelines

Here is the website: https://mavenhollowcare.com/

Here are some words for the ad - feel free to use creative liberties if you have something better or need less words.

1. The Future of Aging is Here

2. Dementia At-Home Care

3. Benefits of an Assisted Living from the Privacy of Your Home - link to

4. Idaho's New Senior Care Option

5. The Security of Senior Living from the Comfort of Your Home

I have the images for all website photos, if you need more images, please let me know.

Target Market(s)

Women age 55+

Industry/Entity Type

Graphic Design

Requirements
Must have
• Incorporate website imagery as much as possible
Should not have
• a feeling of helplessness, old, etc.

```html
<!DOCTYPE html>
<html lang="en">
<head>
<meta charset="utf-8">
<title>Maven Hollow – Banner Ad Set</title>
<link rel="stylesheet" href="https://fonts.googleapis.com/css2?family=Arimo:wght@400&display=swap">
<style>
  :root {
    --stage: #262626;
    --white: #ffffff;
    --ink: #111111;
    --gold: rgba(176, 124, 8, 0.88);
    --gold-solid: #b07c08;
    --button: #000000;
    --button-frame: rgba(255, 255, 255, 0.85);
  }
  * { box-sizing: border-box; margin: 0; padding: 0; }
  html, body { width: 1200px; height: 1200px; overflow: hidden; }
  body {
    background: var(--stage);
    font-family: "Arimo", Helvetica, Arial, sans-serif;
    position: relative;
  }
  .ad { position: absolute; overflow: hidden; background: var(--white); }
  .photo { position: absolute; }
  .brand {
    position: absolute;
    color: var(--ink);
    font-weight: 400;
    letter-spacing: 0.02em;
    line-height: 1;
    display: flex;
    align-items: center;
    justify-content: center;
    text-align: center;
  }
  .caption {
    position: absolute;
    background: var(--gold);
    color: var(--white);
    line-height: 1.05;
    display: flex;
    align-items: center;
  }
  .cta {
    position: absolute;
    border: 1px solid var(--button-frame);
    padding: 4px;
  }
  .cta span {
    display: flex;
    align-items: center;
    justify-content: center;
    width: 100%;
    height: 100%;
    background: var(--button);
    color: var(--white);
  }

  /* Wide skyscraper */
  .skyscraper { left: 146px; top: 129px; width: 167px; height: 637px; }
  .skyscraper .brand { left: 0; top: 0; width: 167px; height: 87px; font-size: 22px; }
  .skyscraper .photo { left: 0; top: 87px; width: 167px; height: 550px;
    background: linear-gradient(180deg, #9c8e6e 0%, #c9b6a0 30%, #a39a96 55%, #4d4a55 80%, #7a6a5a 100%); }
  .skyscraper .caption { left: 13px; top: 459px; width: 144px; height: 92px; padding: 0 12px; font-size: 22px; background: rgba(70, 52, 10, 0.82); }
  .skyscraper .cta { left: 25px; top: 570px; width: 115px; height: 44px; font-size: 14px; }

  /* Large rectangle */
  .large-rect { left: 374px; top: 129px; width: 318px; height: 637px; }
  .large-rect .brand { left: 0; top: 0; width: 318px; height: 115px; font-size: 36px; }
  .large-rect .photo { left: 0; top: 115px; width: 318px; height: 522px;
    background: linear-gradient(160deg, #3a2e28 0%, #8a6a58 35%, #b48e78 55%, #6a5244 75%, #4a3c33 100%); }
  .large-rect .caption { left: 31px; top: 459px; width: 260px; height: 92px; justify-content: center; text-align: center; font-size: 20px; padding: 0 8px; background: rgba(140, 96, 10, 0.8); }
  .large-rect .cta { left: 106px; top: 571px; width: 114px; height: 42px; font-size: 14px; }

  /* Medium rectangle */
  .medium-rect { left: 746px; top: 502px; width: 317px; height: 264px; }
  .medium-rect .photo { inset: 0;
    background: linear-gradient(90deg, #6a5a52 0%, #b39a8c 25%, #d9d8c0 55%, #e3e6cf 100%); }
  .medium-rect .brand { left: 150px; top: 20px; width: 160px; height: 70px; font-size: 26px; }
  .medium-rect .caption { left: 158px; top: 116px; width: 159px; height: 56px; justify-content: center; text-align: center; font-size: 16px; background: var(--gold-solid); }
  .medium-rect .cta { left: 191px; top: 214px; width: 96px; height: 35px; font-size: 12px; padding: 3px; }

  /* Leaderboard */
  .leaderboard { left: 66px; top: 909px; width: 773px; height: 94px; }
  .leaderboard .brand { left: 0; top: 0; width: 222px; height: 94px; font-size: 30px; }
  .leaderboard .photo { left: 222px; top: 0; width: 551px; height: 94px;
    background: linear-gradient(90deg, #3a2014 0%, #a2461a 30%, #e0802a 45%, #6a2a18 60%, #c0701e 85%, #a85a1c 100%); }
  .leaderboard .caption { left: 571px; top: 19px; width: 178px; height: 56px; padding: 0 10px; font-size: 15px; background: var(--gold-solid); }
  .leaderboard .cta { left: 234px; top: 48px; width: 80px; height: 28px; font-size: 10px; padding: 0; border-color: rgba(255,255,255,0.6); }
  .leaderboard .cta span { background: rgba(0,0,0,0.55); }

  /* Mobile leaderboard */
  .mobile-board { left: 794px; top: 1033px; width: 340px; height: 54px; }
  .mobile-board .photo { left: 180px; top: 0; width: 160px; height: 54px;
    background: linear-gradient(90deg, #ffffff 0%, #d7d8cc 40%, #b89a8a 70%, #cfd3c3 100%); }
  .mobile-board .brand { left: 0; top: 0; width: 104px; height: 54px; font-size: 15px; }
  .mobile-board .headline { position: absolute; left: 110px; top: 8px; font-size: 12px; line-height: 1.05; color: var(--ink); }
  .mobile-board .cta { left: 170px; top: 28px; width: 49px; height: 16px; font-size: 6px; padding: 1px; border-color: #999; }
</style>
</head>
<body>

<section class="ad skyscraper" aria-label="Wide skyscraper 160x600">
  <div class="brand">Maven Hollow</div>
  <div class="photo" role="img" aria-label="Smiling senior woman with a blue scarf sitting outdoors among red flowers"></div>
  <p class="caption">Idaho's New Senior Care Option</p>
  <a class="cta" href="https://mavenhollowcare.com/"><span>Learn More</span></a>
</section>

<section class="ad large-rect" aria-label="Large rectangle 300x600">
  <div class="brand">Maven Hollow</div>
  <div class="photo" role="img" aria-label="A younger hand gently resting on an older person's hands over a woven blanket"></div>
  <p class="caption">The Security of Senior Living from the Comfort of Your Home</p>
  <a class="cta" href="https://mavenhollowcare.com/"><span>Learn More</span></a>
</section>

<section class="ad medium-rect" aria-label="Medium rectangle 300x250">
  <div class="photo" role="img" aria-label="Portrait of a senior man with a white moustache, arms crossed, against a pale background"></div>
  <div class="brand">Maven Hollow</div>
  <p class="caption">The Future of Aging is Here</p>
  <a class="cta" href="https://mavenhollowcare.com/"><span>Learn More</span></a>
</section>

<section class="ad leaderboard" aria-label="Leaderboard 728x90">
  <div class="brand">Maven Hollow</div>
  <div class="photo" role="img" aria-label="Feet in red patterned wool socks warming by a glowing fireplace"></div>
  <a class="cta" href="https://mavenhollowcare.com/"><span>Learn More</span></a>
  <p class="caption">Benefits of an Assisted Living from the Privacy of Your Home</p>
</section>

<section class="ad mobile-board" aria-label="Mobile leaderboard 320x50">
  <div class="photo" role="img" aria-label="Portrait of a senior man against a pale background"></div>
  <div class="brand">Maven Hollow</div>
  <p class="headline">Dementia<br>At-Home<br>Care</p>
  <a class="cta" href="https://mavenhollowcare.com/"><span>Learn More</span></a>
</section>

</body>
</html>
```